Zielgruppe
Wir sind ein Liechtensteiner Personaldienstleisungsunternehmen welches sowohl in der klassischen Personalvermittlung als auch in der temporären Personalbereitstellung tätig ist. Unsere Branchen reichen von Baugewerbe, Handwerk, Gastro- und Hotelerie bis hin zu Produktion und Gesundheitswesen.
Achtung:
Habe gerade die files vom neuen Logo hochgeladen!!!
Aufgabenstellung
Visitienkarten designen.
Briefpapier Vorlagenerstellung.
Schlichtes Visitenkartendesign Business auf der nicht zuviele Informationen sind (das Wichtigste)
Vorderseite:
Logo (wird vor Abschluss noch in besserer Qualität hochgeladen)
Firmenname
Anschrift
Name
Funktion
Telefon
Fax
E-Mail
Homepage
Rückseite:
Kann Kreativ gestaltet werden, farblich (blau, gelb, schwarz, weiss), nach Möglichkeit keinen weissen Hintergrund.
!!Bitte keine Vorschläge mit dem Fotoscanner ... da! Danke.
Wir freuen uns auch auf kreative Vorschläge, welche etwas vom Briefing abweichen.
TKV - Team

```html
<!DOCTYPE html>
<html lang="de">
<head>
<meta charset="utf-8">
<title>TKV Personal – Geschäftsausstattung</title>
<link rel="stylesheet" href="https://fonts.googleapis.com/css2?family=Open+Sans:wght@400;600;700&display=swap">
<style>
  :root {
    --stage: #6b6b6b;
    --paper: #ffffff;
    --brand-blue: #2a5db0;
    --brand-deep: #1f4fa3;
    --brand-sky: #4aa8e0;
    --brand-lilac: #a9acd9;
    --accent-sun: #f5c400;
    --text-blue: #1f4a9c;
  }
  * { margin: 0; padding: 0; box-sizing: border-box; }
  html, body { width: 1200px; height: 900px; overflow: hidden; }
  body {
    background: var(--stage);
    font-family: "Open Sans", Arial, sans-serif;
    color: var(--text-blue);
    position: relative;
  }
  .sheet {
    position: absolute;
    background: var(--paper);
    overflow: hidden;
    box-shadow: 0 4px 14px rgba(0,0,0,.45);
  }
  .sheet svg.decor { position: absolute; left: 0; top: 0; }

  /* Wordmark */
  .wordmark {
    position: absolute;
    display: flex;
    align-items: center;
    gap: 8px;
    color: var(--brand-blue);
    font-weight: 700;
    white-space: nowrap;
    line-height: 1.2;
  }
  .wordmark .dot {
    width: 14px; height: 14px; border-radius: 50%;
    background: var(--accent-sun);
    flex: none;
  }

  /* Card back */
  .card-back { left: 56px; top: 136px; width: 475px; height: 315px; }
  .card-back .wordmark { left: 50%; top: 52px; transform: translateX(-50%); font-size: 36px; }

  /* Card front */
  .card-front { left: 56px; top: 479px; width: 475px; height: 315px; }
  .card-front .team-visual {
    position: absolute; left: 113px; top: 22px; width: 247px; height: 104px;
    background: linear-gradient(180deg, #8f98d6 0%, #5b6cc0 100%);
    opacity: .75;
    border-radius: 4px;
  }
  .card-front .wordmark { left: 50%; top: 136px; transform: translateX(-50%); font-size: 28px; }
  .contact-person { position: absolute; left: 40px; top: 202px; }
  .contact-person .name { font-size: 22px; font-weight: 600; color: var(--brand-deep); line-height: 1.1; }
  .contact-person .role { font-size: 14px; font-weight: 600; color: var(--brand-sky); line-height: 1.3; }
  .contact-person .address { font-size: 15px; font-weight: 600; line-height: 1.25; margin-top: 4px; }
  .contact-lines { position: absolute; left: 276px; top: 206px; font-size: 16.5px; font-weight: 600; line-height: 1.65; }

  /* Letterhead */
  .letterhead { left: 586px; top: 39px; width: 580px; height: 820px; }
  .letterhead .wordmark { right: 40px; top: 74px; font-size: 22px; gap: 6px; }
  .letterhead .wordmark .dot { width: 11px; height: 11px; }
  .sender { position: absolute; left: 418px; top: 126px; font-size: 9.5px; font-weight: 600; line-height: 1.4; }
  .sender .company { margin-bottom: 14px; }
  .bank-details { position: absolute; top: 774px; font-size: 9px; font-weight: 600; line-height: 1.55; }
  .bank-details.primary { left: 28px; }
  .bank-details.secondary { left: 268px; }
</style>
</head>
<body>

<section class="sheet card-back" aria-label="Visitenkarte Rückseite">
  <svg class="decor" width="475" height="315" viewBox="0 0 475 315">
    <defs>
      <linearGradient id="backFill" x1="0" y1="0" x2="0" y2="1">
        <stop offset="0" stop-color="#b4b6e0"/>
        <stop offset="1" stop-color="#2a5cb2"/>
      </linearGradient>
      <linearGradient id="backLine" x1="0" y1="0" x2="1" y2="0">
        <stop offset="0" stop-color="#1f5bb5"/>
        <stop offset="1" stop-color="#4aa8e0"/>
      </linearGradient>
    </defs>
    <path d="M0 110 Q237 236 475 110 L475 315 L0 315 Z" fill="url(#backFill)"/>
    <path d="M0 108 Q237 234 475 108" fill="none" stroke="url(#backLine)" stroke-width="6"/>
  </svg>
  <div class="wordmark"><span class="dot"></span>TKV Personal</div>
</section>

<section class="sheet card-front" aria-label="Visitenkarte Vorderseite">
  <svg class="decor" width="475" height="315" viewBox="0 0 475 315">
    <path d="M0 146 Q237 36 475 146" fill="none" stroke="#3e57a8" stroke-width="5"/>
    <path d="M0 146 Q237 36 475 146" fill="none" stroke="#b9bde6" stroke-width="12" opacity=".45" transform="translate(0,-8)"/>
  </svg>
  <div class="team-visual" role="img" aria-label="Silhouetten einer Gruppe von Geschäftsleuten"></div>
  <div class="wordmark"><span class="dot"></span>TKV Personal</div>
  <div class="contact-person">
    <p class="name">Lukas Berger</p>
    <p class="role">Geschäftsführer</p>
    <p class="address">Rheinblickstrasse 12<br>FL-9490</p>
  </div>
  <div class="contact-lines">
    <p>Tel. +423 555 12 00</p>
    <p>Fax. +423 555 12 01</p>
    <p>Email: office@tkv.li</p>
  </div>
</section>

<section class="sheet letterhead" aria-label="Briefpapier">
  <svg class="decor" width="580" height="820" viewBox="0 0 580 820">
    <defs>
      <linearGradient id="topBand" x1="0" y1="0" x2="1" y2="0">
        <stop offset="0" stop-color="#1f5bb5"/>
        <stop offset=".45" stop-color="#4a8fd6" stop-opacity=".7"/>
        <stop offset="1" stop-color="#ffffff" stop-opacity="0"/>
      </linearGradient>
      <linearGradient id="cornerBand" x1="0" y1="1" x2="1" y2="0">
        <stop offset="0" stop-color="#2a5cb2"/>
        <stop offset="1" stop-color="#4aa8e0"/>
      </linearGradient>
    </defs>
    <path d="M0 0 L400 0 Q200 8 0 46 Z" fill="url(#topBand)"/>
    <path d="M0 50 Q200 12 400 30" fill="none" stroke="#a9acd9" stroke-width="3" opacity=".7"/>
    <path d="M433 820 Q520 780 580 712 L580 820 Z" fill="url(#cornerBand)"/>
    <path d="M420 820 Q515 775 580 700" fill="none" stroke="#a9acd9" stroke-width="4"/>
  </svg>
  <div class="wordmark"><span class="dot"></span>TKV Personal</div>
  <div class="sender">
    <p class="company">TKV Anstalt</p>
    <p>Rheinblickstrasse 12</p>
    <p>FL-9490</p>
    <p>Tel. +423 555 12 00</p>
    <p>Fax. +423 555 12 01</p>
    <p>Email: office@tkv.li</p>
  </div>
  <div class="bank-details primary">
    <p>Alpenrhein Handelsbank AG</p>
    <p>Kto.Nr. CHF 408.311.62, Kto.Nr. EUR 408.527.19</p>
  </div>
  <div class="bank-details secondary">
    <p>Talstädter Sparkasse</p>
    <p>BLZ 31455, Kto.Nr. 00600004287</p>
  </div>
</section>

</body>
</html>
```